Etiketten für Schaps
Zielgruppe
Erzeugung hochwertiger Spirituosen wie Vodka, Gin, Liköre, Schnäpse. Das Produktporfolio reicht vom klassischem Vodka bis zu Absinth oder Kräuterbitter. Finden Sie unsere Produkte unter: www.brunecker-destille.at
Zielgruppe: Export nach Asien bzw. Afrika an die immer größer werdende Bevölkerungsschicht, die europäische Qualität schätzt. Fokus auf das österr. Image: K. u. K Zeit, Bergfalke, Sissy, Tradition, Kultur
Gesucht wird ein klassisches Spirituosenetikett
Aufgabenstellung
Gestaltung eines Vorderetiketts für eine eckige Flasche mit schwarzer Kapsel mit goldenem Aufdruck.
Verwendung des Logos 'B - Bergfalke ' (siehe Anlage), es soll jedoch neben Vodka und Gin auch eine Schnapsserie entwickelt werden: Sorten: Himbeergeist, Marillenschnaps, Williams-Christ-Birnenschnaos, Obstschnaps, Haselnuss-Schnaps
Größe des Etiketts: konisch, Breite oben: 53mm, Breite unten: 40 mll, Länge: max 150 mm, Ränder gewölbt, siehe
Stanze (siehe Anlage).
Die Farbe sollte in den Farben Gold/Schwarz gehalten werden, ev. auch eine rot-weiß-rote Fahne o.ä. als Hinweis auf die Herkunft
Ev. auch mit Fruchtabbildungen, diese können auch aus kommerziellen Bilddatenbanken genommen werden.

```html
<!DOCTYPE html>
<html lang="de">
<head>
<meta charset="utf-8">
<title>Bergfalke Haselnuss Schnaps – Etiketten</title>
<link href="https://fonts.googleapis.com/css2?family=Playfair+Display:wght@700;900&family=Lato:wght@400&family=Great+Vibes&display=swap" rel="stylesheet">
<style>
  :root {
    --paper: #ffffff;
    --outline: #a8a8a8;
    --band-light: #3a3a3a;
    --band-dark: #1b1b1b;
    --black: #000000;
    --gold: #c9a54a;
    --gold-light: #f0dc8a;
    --gold-dark: #8a6a2a;
    --flag-red: #a8323a;
    --flag-white: #ffffff;
  }
  html, body { margin: 0; padding: 0; overflow: hidden; background: var(--paper); }
  .sheet { display: block; width: 1200px; height: 2990px; }
  .die-line { fill: none; stroke: var(--outline); stroke-width: 1.5; }
  .band { fill: url(#band-tones); }
  .seal-back { fill: var(--black); }
  .seal-ring { fill: none; stroke: url(#gold-tones); }
  .brand-name { font-family: "Lato", sans-serif; font-weight: 400; fill: var(--gold); letter-spacing: 1px; }
  .title-plaque { fill: var(--black); stroke: url(#gold-tones); stroke-width: 5; }
  .title-text { font-family: "Playfair Display", serif; font-weight: 900; fill: var(--gold); }
  .premium { font-family: "Great Vibes", cursive; fill: var(--gold); }
  .portrait-ring { fill: none; stroke: var(--gold); stroke-width: 4; }
</style>
</head>
<body>
<svg class="sheet" viewBox="0 0 1200 2990" xmlns="http://www.w3.org/2000/svg">
  <defs>
    <linearGradient id="gold-tones" x1="0" y1="0" x2="1" y2="1">
      <stop offset="0" stop-color="#8a6a2a"/>
      <stop offset="0.45" stop-color="#f0dc8a"/>
      <stop offset="1" stop-color="#a3802f"/>
    </linearGradient>
    <radialGradient id="band-tones" cx="0.5" cy="0.5" r="0.8">
      <stop offset="0" stop-color="#363636"/>
      <stop offset="0.6" stop-color="#2a2a2a"/>
      <stop offset="1" stop-color="#1b1b1b"/>
    </radialGradient>
    <radialGradient id="nut-tones" cx="0.55" cy="0.5" r="0.6">
      <stop offset="0" stop-color="#e7d3b3"/>
      <stop offset="0.35" stop-color="#a8592c"/>
      <stop offset="0.7" stop-color="#7a3e1e"/>
      <stop offset="1" stop-color="#5f9a3a" stop-opacity="0.9"/>
    </radialGradient>
    <radialGradient id="portrait-tones" cx="0.5" cy="0.4" r="0.65">
      <stop offset="0" stop-color="#f4f4f4"/>
      <stop offset="0.55" stop-color="#cfcfcf"/>
      <stop offset="1" stop-color="#5a5a5a"/>
    </radialGradient>
  </defs>

  <!-- Front label -->
  <g class="front-label">
    <rect class="die-line" x="116" y="190" width="899" height="1498"/>
    <rect class="band" x="387" y="188" width="358" height="1502" role="img" aria-label="Dunkles Damastmuster"/>

    <g class="seal" transform="translate(565 583)">
      <ellipse class="seal-back" rx="235" ry="276"/>
      <ellipse class="seal-ring" rx="212" ry="252" stroke-width="16"/>
      <text class="brand-name" y="18" font-size="54" text-anchor="middle">BERGFALKE</text>
    </g>

    <ellipse cx="565" cy="969" rx="98" ry="92" fill="url(#nut-tones)" role="img" aria-label="Haselnüsse mit grünen Blättern"/>

    <g class="title" transform="translate(563 1158) rotate(-8.5)">
      <rect class="title-plaque" x="-216" y="-76" width="432" height="152"/>
      <text class="title-text" y="-6" font-size="66" text-anchor="middle" textLength="396" lengthAdjust="spacingAndGlyphs">HASELNUSS</text>
      <text class="title-text" y="58" font-size="66" text-anchor="middle" textLength="310" lengthAdjust="spacingAndGlyphs">SCHNAPS</text>
    </g>
    <text class="premium" x="566" y="1312" font-size="70" text-anchor="middle" transform="rotate(-15 566 1295)">Premium</text>

    <circle cx="562" cy="1450" r="92" fill="url(#portrait-tones)" role="img" aria-label="Historisches Porträt in Uniform"/>
    <circle class="portrait-ring" cx="562" cy="1450" r="92"/>

    <g class="flag">
      <rect x="492" y="1600" width="142" height="39" fill="var(--flag-white)"/>
      <rect x="498" y="1606" width="130" height="9" fill="var(--flag-red)"/>
      <rect x="498" y="1625" width="130" height="9" fill="var(--flag-red)"/>
    </g>
  </g>

  <!-- Cap sticker -->
  <g class="cap-sticker">
    <circle class="die-line" cx="268" cy="2060" r="157"/>
    <g transform="translate(268 2060)">
      <ellipse class="seal-back" rx="124" ry="146"/>
      <ellipse class="seal-ring" rx="110" ry="132" stroke-width="9"/>
      <text class="brand-name" y="10" font-size="30" text-anchor="middle">BERGFALKE</text>
    </g>
  </g>

  <!-- Neck labels -->
  <g class="neck-labels">
    <rect class="die-line" x="108" y="2248" width="998" height="599"/>
    <rect class="band" x="159" y="2249" width="243" height="597" role="img" aria-label="Dunkles Damastmuster"/>
    <rect class="band" x="487" y="2249" width="243" height="597" role="img" aria-label="Dunkles Damastmuster"/>
    <rect class="band" x="815" y="2249" width="243" height="597" role="img" aria-label="Dunkles Damastmuster"/>
    <g transform="translate(279 2616)">
      <ellipse class="seal-back" rx="149" ry="164"/>
      <ellipse class="seal-ring" rx="134" ry="149" stroke-width="10"/>
      <text class="brand-name" y="12" font-size="36" text-anchor="middle">BERGFALKE</text>
    </g>
    <g transform="translate(609 2616)">
      <ellipse class="seal-back" rx="149" ry="164"/>
      <ellipse class="seal-ring" rx="134" ry="149" stroke-width="10"/>
      <text class="brand-name" y="12" font-size="36" text-anchor="middle">BERGFALKE</text>
    </g>
    <g transform="translate(937 2616)">
      <ellipse class="seal-back" rx="149" ry="164"/>
      <ellipse class="seal-ring" rx="134" ry="149" stroke-width="10"/>
      <text class="brand-name" y="12" font-size="36" text-anchor="middle">BERGFALKE</text>
    </g>
  </g>
</svg>
</body>
</html>
```